Local fast-growing company in the service sector

We are looking for a modern business card design, which should also appear on our letterheads

Target Market(s)

Private and industrial sectors

Contact Information for Business Card

Vorname Name
Lindkofer Str. 18
71468 Waiblingen
Tel.: 07163-418259-0
Name@kovaltec-pbz.de

Colors
9d9d9d
919191
aaaaaa

Requirements
Must have
• The logo (file) in silver

```html
<!DOCTYPE html>
<html lang="de">
<head>
<meta charset="utf-8">
<title>Kovaltec Hausservice – Visitenkarte</title>
<link rel="stylesheet" href="https://fonts.googleapis.com/css2?family=Raleway:wght@300;400;600&display=swap">
<style>
  :root {
    --backdrop: #a3a3a3;
    --card: #ffffff;
    --ink: #3a3a3a;
    --silver: #9d9d9d;
    --silver-dark: #919191;
    --silver-light: #aaaaaa;
  }
  * { margin: 0; padding: 0; box-sizing: border-box; }
  html, body {
    width: 1200px;
    height: 1200px;
    overflow: hidden;
    background: var(--backdrop);
    font-family: "Raleway", sans-serif;
    color: var(--ink);
  }
  .business-card {
    position: absolute;
    left: 307px;
    top: 147px;
    width: 586px;
    height: 906px;
    background: var(--card);
  }
  .brand {
    position: absolute;
    left: 53px;
    top: 96px;
    display: flex;
    align-items: center;
    gap: 18px;
  }
  .brand-square {
    width: 58px;
    height: 58px;
    background: var(--silver-light);
  }
  .brand-name {
    font-weight: 600;
    font-size: 62px;
    letter-spacing: 2px;
    color: var(--silver);
    line-height: 1;
  }
  .person {
    position: absolute;
    left: 53px;
    top: 366px;
  }
  .person-name {
    font-weight: 300;
    font-size: 31px;
    letter-spacing: 1px;
    line-height: 1.2;
  }
  .person-role {
    margin-top: 10px;
    font-weight: 400;
    font-size: 20px;
  }
  .contact-list {
    position: absolute;
    left: 53px;
    top: 472px;
    list-style: none;
  }
  .contact-item {
    display: flex;
    align-items: center;
    gap: 12px;
    height: 37px;
    font-weight: 400;
    font-size: 21px;
  }
  .contact-icon {
    width: 21px;
    height: 21px;
    flex: none;
  }
  .company-address {
    position: absolute;
    left: 53px;
    top: 758px;
    font-style: normal;
    font-weight: 400;
    font-size: 21px;
    line-height: 34.5px;
  }
</style>
</head>
<body>
  <main class="business-card">
    <div class="brand">
      <div class="brand-square"></div>
      <div class="brand-name">KOVALTEC</div>
    </div>

    <section class="person">
      <h1 class="person-name">MAX MUSTERMANN</h1>
      <p class="person-role">Geschäftsführer</p>
    </section>

    <ul class="contact-list">
      <li class="contact-item">
        <svg class="contact-icon" viewBox="0 0 24 24" aria-hidden="true">
          <path fill="var(--silver-light)" d="M3 9c0-3 4-5 9-5s9 2 9 5v2h-5V9c-1-1-2.5-1.3-4-1.3S9 8 8 9v2H3z"/>
          <rect x="5" y="12" width="14" height="8" rx="1.5" fill="var(--silver-light)"/>
          <circle cx="12" cy="16" r="2.2" fill="#fff"/>
        </svg>
        <span>07163-418259-0</span>
      </li>
      <li class="contact-item">
        <svg class="contact-icon" viewBox="0 0 24 24" aria-hidden="true">
          <rect x="2" y="5" width="20" height="14" rx="1" fill="var(--silver-light)"/>
          <path d="M2.5 5.5 12 13l9.5-7.5M2.5 18.5 9.5 11M21.5 18.5 14.5 11" stroke="#fff" stroke-width="1.4" fill="none"/>
        </svg>
        <span>Name@kovaltec-pbz.de</span>
      </li>
      <li class="contact-item">
        <svg class="contact-icon" viewBox="0 0 24 24" aria-hidden="true">
          <circle cx="12" cy="12" r="9.5" fill="var(--silver-light)"/>
          <g stroke="#fff" stroke-width="1.2" fill="none">
            <ellipse cx="12" cy="12" rx="4" ry="9.5"/>
            <path d="M2.5 12h19M4 7.5h16M4 16.5h16M12 2.5v19"/>
          </g>
        </svg>
        <span>www.kovaltec-pbz.de</span>
      </li>
    </ul>

    <address class="company-address">
      Kovaltec Hausservice GmbH &amp; Co. KG<br>
      Lindkofer Str. 18<br>
      71468 Waiblingen
    </address>
  </main>
</body>
</html>
```